Stationery Design Project

We need a stationery design for our Norwegian trucking company. We have existed for about 15 years and our 12 drivers uses relatively new vehicles to transport goods around in northern Norway. Long distance routes with fresh fish og food transport is our main operations.

We have already made alogo that's printed on our trucks. The logo and a picture of our trucks is attached. I think the logo i crappy, but since its already in use, changing it is not an option in this round. Still using a better colour scheme in the overall stationery and more interesting fonts is possible (altso in the logo).

Company details:
Name: Vikstrandbil AS
Organisation nr 981 537 608
Post adress: 8613 Lysvær

I like minimalism and simplicity. I am avalibly for questions in normal GMT working hours either here or on mail: petter@vikstrand.no

Reason: Hi. Im extending the deadline because I needed some time to find a vector file of our logo. Sorry for the inconvenience

Hi, and thanks for all your interest in the project. Some updates:

-          I have decided to commit to using one of the designs. Some designer will get the payment.

-          I have extended the deadline with 24 hours since I needed some time to find our firms vector logo (a slow Swedish man was holding me up)

-          We will not choose a design before the deadline. No need to rush.

-          We have received a lot of great design and think there is a need to specified the product we want to make:

o   Business Card for all our employers. I just need the design and will duplicate with the correct numbers and name myself. The information on should be: Logo, employer’s name, Phone number, email, website, Postal number and address. Use this as a template: logo, Leif Brattli, 47283916, Leif@vikstrand.no,, vikstrand.no, 8613 Lysvær. The order and placement of the information is your creative decision.

o   Stickers to put on the goods we travel. On the sticker the should be the following information: Logo, phone number, Tekst and link: Fraktæ av Vikstrandbil. Ke du syns? Vikstrand.no/tilbakemelding (this means: Handled by Vikstrandbil. What do you think Vikstrand.no/feedback -à the link will be a feedback form). The placement the information and size is your creative decision with some stings: we have been thinking of using Prentavo for printing and see that a size about 6x6 cm, 8x5 or something like that. (with 3000 copies our budget is 200 punds). Any suggestions of other suppliers are welcome. Prentavo price calculator http://www.prentavoprint.co.uk/digital-litho-printing/printing-labels-tags/stickers/

o   Letterhead with logo, address, phone number and organizational number.

o   Envelopes with logo,address, phone number and organizational number.

Have a nice day.

 

 

• Using the blue colour in the logo and using a similar graphic approch.

```html
<!DOCTYPE html>
<html lang="no">
<head>
<meta charset="utf-8">
<title>Vikstrandbil AS – Stationery</title>
<link rel="stylesheet" href="https://fonts.googleapis.com/css2?family=Crimson+Text:ital,wght@0,400;0,600;0,700;1,400&display=swap">
<style>
  :root {
    --backdrop: #cbcbcb;
    --paper: #ffffff;
    --navy: #0c0087;
    --royal: #2a55d6;
    --sky: #0a8fd6;
    --ink: #111111;
    --serif: "Crimson Text", "Palatino Linotype", Georgia, serif;
  }
  * { box-sizing: border-box; margin: 0; padding: 0; }
  html, body { width: 1200px; height: 1000px; overflow: hidden; }
  body { background: var(--backdrop); font-family: var(--serif); position: relative; }

  .sheet { position: absolute; background: var(--paper); overflow: hidden; }

  .wave-band {
    position: absolute; left: 0; right: 0; bottom: 0;
    background: linear-gradient(to top, var(--navy) 0%, var(--navy) 45%, var(--royal) 75%, var(--sky) 100%);
  }

  .wordmark {
    position: absolute; font-family: var(--serif); font-weight: 700;
    color: var(--royal); white-space: nowrap; line-height: 1;
  }
  .wordmark::before {
    content: ""; display: inline-block; width: .55em; height: .55em;
    border-radius: 50%; background: currentColor; margin-right: .3em; vertical-align: .05em;
  }

  .footer-line {
    position: absolute; color: var(--paper); font-style: italic;
    font-size: 8.5px; white-space: nowrap;
  }

  /* Letterhead */
  .letterhead { left: 50px; top: 185px; width: 490px; height: 690px; }
  .letterhead .wave-band { height: 120px; }
  .letterhead .wordmark { right: 26px; top: 44px; font-size: 22px; }
  .letterhead .footer-line { right: 32px; bottom: 16px; }

  /* Envelope */
  .envelope { left: 590px; top: 645px; width: 560px; height: 237px; }
  .envelope .wave-band { height: 90px; }
  .envelope .wordmark { left: 26px; top: 32px; font-size: 22px; }
  .envelope .footer-line { left: 26px; bottom: 10px; }

  /* Business card back */
  .card-back { left: 695px; top: 195px; width: 312px; height: 178px; background: var(--navy); }
  .card-back .wave-band { height: 30px; background: var(--royal); }
  .card-back .wordmark { left: 50%; top: 74px; transform: translateX(-50%); font-size: 22px; color: var(--sky); }

  /* Business card front */
  .card-front { left: 695px; top: 397px; width: 312px; height: 178px; }
  .card-front .wave-band { height: 34px; background: linear-gradient(to top, var(--royal) 0%, var(--royal) 55%, var(--sky) 100%); }
  .card-front .wordmark { right: 22px; top: 44px; font-size: 16px; }
  .contact { position: absolute; left: 20px; top: 36px; color: var(--ink); }
  .contact-company { color: var(--navy); font-weight: 600; font-size: 9.5px; letter-spacing: 1.6px; }
  .contact-role { font-style: italic; font-size: 7px; letter-spacing: 1px; margin: 2px 0 0 34px; }
  .contact-list { list-style: none; margin-top: 10px; font-size: 7px; font-style: italic; letter-spacing: .8px; line-height: 8.5px; }
  .contact-list b { display: inline-block; width: 20px; color: var(--navy); font-weight: 700; font-style: normal; }
</style>
</head>
<body>

<section class="sheet letterhead" aria-label="Letterhead">
  <div class="wave-band" role="img" aria-label="Blue wave band decoration along the foot of the page"></div>
  <div class="wordmark">Vikstrandbil</div>
  <p class="footer-line">Vikstrandbil AS, Organisation NR 981 537 608 8613 Lysvær</p>
</section>

<section class="sheet card-back" aria-label="Business card, back">
  <div class="wave-band" role="img" aria-label="Blue wave band decoration along the card edge"></div>
  <div class="wordmark">Vikstrandbil</div>
</section>

<section class="sheet card-front" aria-label="Business card, front">
  <div class="wave-band" role="img" aria-label="Blue wave band decoration along the card edge"></div>
  <div class="contact">
    <p class="contact-company">VIKSTRANDBIL</p>
    <p class="contact-role">Mkting. Director</p>
    <ul class="contact-list">
      <li><b>p:</b>+47 063 41200</li>
      <li><b>m:</b>+47 063 41200</li>
      <li><b>e:</b>petter@vikstrand.no</li>
      <li><b>w:</b>www.vikstrand.no</li>
    </ul>
  </div>
  <div class="wordmark">Vikstrandbil</div>
</section>

<section class="sheet envelope" aria-label="Envelope">
  <div class="wave-band" role="img" aria-label="Blue wave band decoration along the foot of the envelope"></div>
  <div class="wordmark">Vikstrandbil</div>
  <p class="footer-line">Vikstrandbil AS, Organisation NR 981 537 608 8613 Lysvær</p>
</section>

</body>
</html>
```